Course Graduation Certificate

This project is not for a flyer but instead for the creation of a course graduation certificate. The final certificate needs to include the Marrow Summit Aviation Academy logo and the text stating as follows:
Certifies that ___________________________ has satisfactorily completed the course of _______________________________ on ________________________________
I would also like to include some type of gold seal of completion as well as a place to sign my name and credentials at the bottom of the certificate
I have included the Marrow Summit Aviation Academy logo as well as three other certificate examples for you to work from.
Target Market(s)
Students completing a certification course and receiving a certificate

```html
<!DOCTYPE html>
<html lang="en">
<head>
<meta charset="UTF-8">
<title>Certificate of Graduation</title>
<link rel="stylesheet" href="https://fonts.googleapis.com/css2?family=Marcellus&family=Playfair+Display:ital@1&family=Poppins:wght@400;600&family=Libre+Baskerville&display=swap">
<style>
  :root{
    --backdrop:#a9a9a9;
    --paper:#fdfaf3;
    --paper-edge:#e8c9a7;
    --guilloche:#c9cfe6;
    --guilloche-dark:#3a4f9c;
    --navy:#2c3d8f;
    --ink:#1a1a1a;
    --script:#4a4040;
    --flourish:#6b5a55;
    --rule:#8a8a8a;
    --plane:#e6e6e6;
    --gold-1:#f3d77a;
    --gold-2:#b88a22;
    --seal-core:#1e1e1e;
  }
  *{box-sizing:border-box;margin:0;padding:0}
  html,body{width:800px;height:1200px;overflow:hidden;background:var(--backdrop)}
  .certificate{
    position:absolute;left:50px;top:330px;width:700px;height:540px;
    background:var(--paper);
    border-left:4px solid var(--paper-edge);border-right:4px solid var(--paper-edge);
  }
  .border-frame{position:absolute;inset:0;width:700px;height:540px}
  .abs{position:absolute}
  .center{left:0;width:700px;text-align:center}
  .flourish{background:var(--flourish);opacity:.35;border-radius:50%}
  .title{top:138px;font-family:"Marcellus",serif;font-size:38px;font-weight:400;color:var(--navy);letter-spacing:1px;line-height:1}
  .subtitle{top:180px;font-family:"Marcellus",serif;font-size:16px;font-weight:400;color:var(--script);letter-spacing:1px;line-height:1}
  .script{font-family:"Playfair Display",serif;font-style:italic;color:var(--script)}
  .certifies{top:212px;font-size:15px;line-height:1.3}
  .field{font-family:"Poppins",sans-serif;font-weight:600;font-size:12px;color:var(--ink);line-height:1}
  .recipient{top:243px}
  .completed{top:276px;font-size:14px;line-height:1.3}
  .course{top:309px}
  .rule{height:1px;background:var(--rule);left:106px;width:490px}
  .on{left:260px;top:340px;font-size:11px;line-height:1.3;color:var(--navy)}
  .date{left:282px;top:343px;font-size:10px}
  .date-rule{left:282px;top:356px;width:164px;height:1px;background:#c8c8c8}
  .seal{left:144px;top:362px;width:64px;height:64px;border-radius:50%;
    background:radial-gradient(circle,var(--gold-1) 0,var(--gold-2) 100%);}
  .seal::after{content:"";position:absolute;inset:9px;border-radius:50%;background:var(--seal-core);border:2px solid var(--gold-1)}
  .motto{left:96px;top:429px;width:160px;text-align:center;font-family:"Libre Baskerville",serif;font-size:7px;line-height:1.25;color:#333}
  .academy-name{left:262px;top:394px;width:150px;text-align:center;font-family:"Poppins",sans-serif;font-weight:600;font-size:11px;line-height:1.25;color:var(--navy)}
  .signature-area{left:478px;top:383px;width:104px;height:32px;background:linear-gradient(90deg,rgba(44,61,143,.18),rgba(44,61,143,.04))}
  .signatory{left:426px;top:420px;width:158px;text-align:center;font-family:"Poppins",sans-serif;font-size:8.5px;line-height:1.35;color:var(--ink)}
  .signatory strong{font-weight:600}
  .plane-art{left:478px;top:137px;width:135px;height:85px;background:radial-gradient(ellipse,var(--plane) 0,rgba(230,230,230,0) 70%)}
</style>
</head>
<body>
  <main class="certificate">
    <svg class="border-frame" viewBox="0 0 700 540">
      <g role="img" aria-label="Blue guilloche border pattern">
        <path fill="var(--guilloche)" fill-rule="evenodd" d="M10 7H693V534H10Z M60 70H642V474H60Z"/>
      </g>
      <rect x="10" y="7" width="683" height="527" fill="none" stroke="var(--guilloche-dark)" stroke-width="1"/>
      <rect x="60" y="70" width="582" height="404" fill="var(--paper)" stroke="var(--guilloche-dark)" stroke-width="1.2"/>
      <rect x="65" y="75" width="572" height="394" fill="none" stroke="var(--guilloche-dark)" stroke-width="0.8"/>
    </svg>

    <div class="abs plane-art" role="img" aria-label="Faint illustration of a small propeller aircraft"></div>

    <div class="abs flourish" style="left:265px;top:112px;width:176px;height:14px" role="img" aria-label="Decorative scroll flourish"></div>
    <h1 class="abs center title">CERTIFICATE</h1>
    <div class="abs flourish" style="left:200px;top:184px;width:46px;height:8px" role="img" aria-label="Decorative scroll flourish"></div>
    <p class="abs center subtitle">OF GRADUATION</p>
    <div class="abs flourish" style="left:456px;top:184px;width:46px;height:8px" role="img" aria-label="Decorative scroll flourish"></div>

    <p class="abs center script certifies">Certifies that</p>
    <p class="abs center field recipient">Dylan Marsh</p>
    <div class="abs rule" style="top:259px"></div>

    <p class="abs center script completed">has satisfactorily completed the course of</p>
    <p class="abs center field course">Vantage 300, 135 INHC</p>
    <div class="abs rule" style="top:325px"></div>

    <span class="abs script on">on</span>
    <span class="abs field date">25th day of July, 2025</span>
    <div class="abs date-rule"></div>

    <div class="abs seal" role="img" aria-label="Gold seal of completion"></div>
    <p class="abs motto">Every safe flight begins<br>with a pilot trained to excel</p>

    <p class="abs academy-name">Marrow Summit<br>Aviation Academy</p>

    <div class="abs signature-area" role="img" aria-label="Handwritten signature"></div>
    <p class="abs signatory">Authorized Signatory<br><strong>Harbor City / Eastbrook Ctr</strong></p>
  </main>
</body>
</html>
```